Morivane Sports K.K. PPT Design (Sales Presentation Template)

We need a PPT design for our new e-commerce sports apparel business that we are launching next month. We have a base design that was used to create our investor pitch deck. I am looking for something that our sales apparatus can use when getting new business. Our clients are professional sports teams. At the moment, our clients are all baseball teams. I would like the deck to use the colors of each baseball team that we present to. For example, The Tobrenn Herons colors are red and blue. I would want the deck to be done in those colors. Our corporate or base colors are yellow and black. Do you you get where I am going with this?

Target Market(s)

professional sports teams. currently Japanese baseball teams.

Industry/Entity Type

Business

Requirements
Must have
• 1. base black and yellow corporate colors as well as our logo
• 2. 12 different variations for the 12 baseball teams here in Japan:
• 1. Valdeno Titans
• 2. Quorvel Ravens
• 3. Tobrenn Herons
• 4. Belcastro Pike
• 5. Ferul Pumas
• 6. Pelto Grivan Sailors
• 7. Sandrevo QuLix
• 8. Orvane Malt Strikers
• 9. Zemparo Condors
• 10. Velmora Jaguars
• 11. Tavu Bisonettes
• 12. Plenvoa Griffins
Nice to have
• http://trelvanatlas.example/wp-content/uploads/2012/03/league_chart_2012_v.gif

```html
<!DOCTYPE html>
<html lang="en">
<head>
<meta charset="utf-8">
<title>Morivane Sports K.K. — Sales Presentation Template</title>
<link href="https://fonts.googleapis.com/css2?family=Raleway:wght@300;400;600;700&family=Open+Sans:wght@400;600;700&display=swap" rel="stylesheet">
<style>
:root{
  --orange:#c84b1f;
  --orange-soft:#e8835a;
  --dark:#2b1219;
  --dark-2:#5a2716;
  --ink:#333;
  --muted:#777;
  --paper:#fff;
  --board-top:#b9babc;
  --board-bottom:#9c9da0;
  --photo-1:#8d8d8d;
  --photo-2:#3e3e3e;
}
*{box-sizing:border-box;margin:0;padding:0}
html,body{width:1200px;height:1200px;overflow:hidden}
body{background:linear-gradient(180deg,var(--board-top),var(--board-bottom));font-family:"Open Sans",sans-serif;color:var(--ink);position:relative}
.slide{position:absolute;width:320px;height:185px;background:var(--paper);box-shadow:4px 5px 6px rgba(0,0,0,.35);overflow:hidden}
.slide--orange{background:var(--orange);color:#fff}
.slide--dark{background:var(--dark);color:#fff}
.hero{left:370px;top:30px;width:480px;height:278px}
.c1{left:40px}.c2{left:440px}.c3{left:850px}
.r1{top:350px}.r2{top:559px}.r3{top:768px}.r4{top:977px}
.title{position:absolute;font-family:"Raleway",sans-serif;font-weight:400;font-size:11px;letter-spacing:.3px;color:#444}
.title b{color:var(--orange);font-weight:400}
.sub{position:absolute;font-size:5px;color:var(--muted)}
.tiny{font-size:3.4px;line-height:4.3px;color:#666}
.brand{position:absolute;left:14px;bottom:8px;font-family:"Raleway",sans-serif;font-weight:700;font-size:5.5px;color:var(--dark);display:flex;align-items:center;gap:3px}
.brand i{display:block;width:7px;height:7px;border-radius:50%;background:var(--dark)}
.team-mark{position:absolute;right:8px;bottom:8px;font-family:"Raleway",sans-serif;font-weight:700;font-size:5px;color:rgba(200,75,31,.25)}
.abs{position:absolute}
.dot{position:absolute;border-radius:50%;display:flex;align-items:center;justify-content:center;color:#fff;font-size:5px}
/* agenda */
.agenda-item{position:absolute;width:48px}
.agenda-item h4{font-size:3.8px;font-weight:400;color:#555;margin-bottom:2px}
/* market */
.stat{position:absolute;top:80px;width:90px;text-align:center}
.stat svg{display:block;margin:0 auto 6px}
.stat strong{display:block;color:var(--orange);font-size:9.5px;font-weight:600}
.stat span{display:block;font-size:5px;color:#333;line-height:6px}
/* team */
.member{position:absolute;top:62px;width:58px;text-align:center}
.portrait{width:54px;height:54px;border-radius:50%;margin:0 auto 4px;border:1.5px solid var(--orange-soft);background:radial-gradient(circle at 50% 40%,#d9d9d9,#3a4150)}
.member b{display:block;font-size:3.4px;color:#333}
.member span{display:block;font-size:3px;color:#777}
.member em{display:block;font-size:3.2px;color:#555;font-style:normal;margin-top:6px}
/* commitment */
.tag{position:absolute;height:9px;font-size:5.3px;color:#fff;padding:1px 0 0 6px}
.tag--orange{background:var(--orange)}
.tag--dark{background:var(--dark)}
.tag span{color:var(--orange)}
.tag--orange span{color:#fff}
/* pointer */
.pointer{position:absolute;width:124px;height:44px}
.pointer .pill{position:absolute;left:20px;top:5px;width:104px;height:34px;border-radius:17px;background:var(--dark);color:#fff;text-align:center;padding:3px 8px 0 18px}
.pointer .pill h5{font-size:3.6px;color:var(--orange-soft);line-height:4.3px}
.pointer .pill p{font-size:3.3px;line-height:4.1px;margin-top:2px}
.pointer .num{position:absolute;left:4px;top:5px;width:34px;height:34px;transform:rotate(45deg) scale(.72);background:var(--orange);border:2px solid #aaa;box-shadow:1px 1px 3px rgba(0,0,0,.4)}
.pointer .num b{position:absolute;inset:0;display:flex;align-items:center;justify-content:center;transform:rotate(-45deg);font-size:15px;color:#fff;font-weight:700;text-shadow:1px 1px 1px #000}
/* meeting */
.bar-label{position:absolute;height:8px;font-size:5.5px;color:#fff;padding:0 0 0 6px;line-height:8px}
.bar-sub{position:absolute;height:6px;background:#8a8a8a;font-size:3.4px;color:#eee;line-height:6px;padding-left:30px}
/* key points */
.kp{position:absolute;width:120px}
.kp .dot{left:0;top:0;width:14px;height:14px;font-size:5px}
.kp h6{position:absolute;left:30px;top:0;font-size:4.3px;font-weight:400;color:var(--orange)}
.kp p{position:absolute;left:30px;top:7px;width:90px}
/* thank you */
.contact{position:absolute;top:128px;width:60px;text-align:center}
.contact .ico{width:22px;height:22px;border-radius:50%;background:var(--orange);border:1.5px solid #fff;margin:0 auto 0;display:flex;align-items:center;justify-content:center}
.contact b{display:block;font-size:5.5px;font-weight:400;margin-top:9px}
.contact span{display:block;font-size:3.5px;line-height:5px;margin-top:3px;color:#ddd}
</style>
</head>
<body>

<!-- Cover -->
<section class="slide hero">
  <svg width="480" height="278" viewBox="0 0 480 278">
    <defs>
      <linearGradient id="stadium" x1="0" y1="0" x2="0" y2="1">
        <stop offset="0" stop-color="#b0b0b0"/><stop offset=".5" stop-color="var(--photo-1)"/><stop offset="1" stop-color="var(--photo-2)"/>
      </linearGradient>
    </defs>
    <rect width="480" height="278" fill="url(#stadium)" role="img" aria-label="Photo of a floodlit baseball stadium full of fans at night"/>
    <polygon points="0,0 232,0 0,278" fill="var(--orange)" opacity=".85"/>
    <polygon points="480,0 480,278 246,278" fill="var(--dark)" opacity=".97"/>
  </svg>
  <div class="abs" style="left:170px;top:118px;width:140px;text-align:center;font-family:'Raleway',sans-serif;font-weight:700;font-size:16px;color:var(--orange);display:flex;align-items:center;justify-content:center;gap:5px;background:rgba(43,18,25,.85);padding:8px 0">
    <i style="display:block;width:10px;height:10px;border-radius:50%;background:var(--orange)"></i>Valdeno Titans
  </div>
</section>

<!-- Agenda -->
<section class="slide c1 r1">
  <h2 class="title" style="left:98px;top:10px;font-size:11px">TODAY’S AGENDA</h2>
  <p class="sub" style="left:98px;top:25px;color:#444">Agenda for this meeting with the team</p>
  <div class="dot" style="left:24px;top:72px;width:24px;height:24px;background:var(--orange)">11:00am</div>
  <div class="dot" style="left:80px;top:60px;width:24px;height:24px;background:var(--dark)">12:00am</div>
  <div class="dot" style="left:135px;top:88px;width:24px;height:24px;background:#8c8c8c">1:30pm</div>
  <div class="dot" style="left:200px;top:67px;width:24px;height:24px;background:var(--orange)">3:00pm</div>
  <div class="dot" style="left:260px;top:55px;width:24px;height:24px;background:var(--dark)">4:00pm</div>
  <div class="agenda-item" style="left:9px;top:110px"><h4>HELLO!</h4><p class="tiny">Short greeting and warm welcome to all guests, then a quick look at what we plan to cover today.</p></div>
  <div class="agenda-item" style="left:68px;top:95px"><h4>BUSINESS</h4><p class="tiny">Overview of our store, the range of team apparel and how orders flow from fans to clubs.</p></div>
  <div class="agenda-item" style="left:125px;top:123px"><h4>LUNCH TIME</h4><p class="tiny">A short break with lunch served in the room, with time to ask questions over food.</p></div>
  <div class="agenda-item" style="left:188px;top:112px"><h4>MARKETING R&amp;D</h4><p class="tiny">How we research fan demand and plan launches around key dates in the season.</p></div>
  <div class="agenda-item" style="left:248px;top:102px"><h4>Q&amp;A</h4><p class="tiny">Open floor for questions, next steps and a plan for the trial run with your club.</p></div>
  <div class="brand"><i></i>MORIVANE</div>
  <div class="team-mark">Titans</div>
</section>

<!-- Market -->
<section class="slide c2 r1">
  <h2 class="abs" style="left:0;right:0;top:24px;text-align:center;font-family:'Raleway',sans-serif;font-weight:700;font-size:8.5px;letter-spacing:1.2px">A SIZEABLE MARKET</h2>
  <div class="abs" style="left:130px;top:37px;width:60px;height:1px;background:#bbb"></div>
  <div class="stat" style="left:17px">
    <svg width="18" height="18" viewBox="0 0 18 18"><rect x="4" y="3" width="10" height="12" rx="5" fill="none" stroke="#555" stroke-width="1.5"/><path d="M4 9h10M7 9v6M11 9v6" stroke="#555" stroke-width="1.2"/></svg>
    <strong>33,000,000</strong><span>Japan-based baseball fans</span>
  </div>
  <div class="stat" style="left:115px">
    <svg width="20" height="18" viewBox="0 0 20 18"><path d="M6 2l-5 3 2 4 2-1v9h10V8l2 1 2-4-5-3c-1 2-7 2-8 0z" fill="#555"/><text x="10" y="13" font-size="6" fill="#fff" text-anchor="middle" font-family="Open Sans">12</text></svg>
    <strong>32,780,000,000</strong><span>Global apparel<br>market</span>
  </div>
  <div class="stat" style="left:213px">
    <svg width="18" height="18" viewBox="0 0 18 18"><path d="M1 3h3l2 9h9l2-7H5" fill="none" stroke="#555" stroke-width="1.5"/><circle cx="7" cy="15" r="1.3" fill="#555"/><circle cx="14" cy="15" r="1.3" fill="#555"/></svg>
    <strong>110,000,000,000</strong><span>Global e-commerce market</span>
  </div>
  <div class="brand"><i></i>MORIVANE</div>
  <div class="team-mark">Titans</div>
</section>

<!-- Team -->
<section class="slide c3 r1">
  <h2 class="title" style="left:20px;top:21px;font-size:8.5px"><b>OUR</b> AMAZING TEAM</h2>
  <p class="sub" style="left:20px;top:35px;font-size:3.4px">Short and brief note on the people who will serve your club</p>
  <div class="member" style="left:18px"><div class="portrait" role="img" aria-label="Portrait of team member"></div><b>RENA OSTVALL</b><span>Creative Lead &amp; Founder</span><em>rena@morivane.example</em></div>
  <div class="member" style="left:89px"><div class="portrait" role="img" aria-label="Portrait of team member"></div><b>TOMAS VELQUIN</b><span>Senior Sales Manager</span><em>tomas@morivane.example</em></div>
  <div class="member" style="left:160px"><div class="portrait" role="img" aria-label="Portrait of team member"></div><b>MR. IDRIS HALLOWAY</b><span>Creative Web Engineer</span><em>idris@morivane.example</em></div>
  <div class="member" style="left:229px"><div class="portrait" role="img" aria-label="Portrait of team member"></div><b>JONAH PRESK</b><span>Creative Graphic Designer</span><em>jonah@morivane.example</em></div>
  <div class="brand"><i></i>MORIVANE</div>
  <div class="team-mark">Titans</div>
</section>

<!-- Why our team -->
<section class="slide c1 r2">
  <h2 class="title" style="left:20px;top:22px;font-size:8.5px">WHY OUR <b>TEAM</b></h2>
  <p class="sub" style="left:20px;top:35px;font-size:3.4px">Short note on what sets this crew apart</p>
  <div class="abs tiny" style="left:20px;top:55px;width:112px">We know the game and the fans. Our crew has years of work in team stores, print and online sales, and we treat each club as a partner, not just a client. Every order gets the same care.</div>
  <div class="abs tiny" style="left:20px;top:87px;width:112px">We move fast from design to shelf. New kits, special event shirts and fan gear go live in days, with stock watched closely so the most wanted items never run out on match day.</div>
  <div class="abs tiny" style="left:20px;top:120px;width:112px">We share clear numbers. Each month your club sees sales, returns and top items, so you can plan ahead and make smart choices.</div>
  <div class="abs" style="left:160px;top:0;width:160px;height:185px;background:linear-gradient(180deg,#d4d4d4,#7a7a7a 55%,#4a4a4a)" role="img" aria-label="Photo of a baseball stadium under floodlights"></div>
  <div class="brand"><i></i>MORIVANE</div>
  <div class="team-mark" style="right:168px">Titans</div>
</section>

<!-- Promises -->
<section class="slide slide--orange c2 r2">
  <h2 class="title" style="left:0;right:0;top:14px;text-align:center;color:#fff;font-size:9px"><span style="color:var(--dark)">OUR</span> PROMISES</h2>
  <p class="abs" style="left:0;right:0;top:30px;text-align:center;font-size:6px">• Lorem ipsum dolor sit amet, alii aliquip ei vel</p>
  <div class="dot" style="left:133px;top:57px;width:46px;height:46px;background:#5c2714;font-size:5.5px">Solution</div>
  <div class="dot" style="left:106px;top:100px;width:44px;height:44px;background:#96371a;font-size:5.5px">Social</div>
  <div class="dot" style="left:164px;top:101px;width:42px;height:42px;background:var(--orange-soft);font-size:5.5px">Satisfaction</div>
  <p class="abs" style="left:19px;top:87px;font-size:4.8px">We must have an answer to help you</p>
  <p class="abs" style="left:214px;top:88px;font-size:4.8px">Connect emotionally with people</p>
</section>

<!-- Commitment -->
<section class="slide c3 r2">
  <h2 class="title" style="left:22px;top:11px;font-size:9.5px">OUR <b>COMMITMENT</b></h2>
  <p class="sub" style="left:22px;top:25px">Now principles discovered off increasing how reasonably</p>
  <div class="tag tag--orange" style="left:22px;top:48px;width:118px">• OUR <span>COMMITMENT</span></div>
  <p class="abs tiny" style="left:28px;top:61px;width:170px">• We keep each promise we make to your club. Orders ship on time, every item is checked, and any fault is fixed fast with no fuss. Staff reply within one working day.</p>
  <div class="tag tag--dark" style="left:64px;top:93px;width:118px">• OUR <span>COMMITMENT</span></div>
  <p class="abs tiny" style="left:70px;top:106px;width:170px">• We protect your brand. Colours, crests and fonts follow your guide exactly, and no design goes live without sign-off from your team first.</p>
  <div class="tag tag--orange" style="left:100px;top:138px;width:118px">• OUR COMMITMENT</div>
  <p class="abs tiny" style="left:106px;top:150px;width:170px;color:var(--orange)">We grow with you. As your fan base grows, our store, stock and service scale up so every fan gets the gear they want on time.</p>
  <div class="brand"><i></i>MORIVANE</div>
  <div class="team-mark">Titans</div>
</section>

<!-- Pointer content -->
<section class="slide c1 r3">
  <h2 class="title" style="left:0;right:0;top:12px;text-align:center;font-size:10px"><b style="font-weight:600">POINTER</b> CONTENT</h2>
  <div class="pointer" style="left:8px;top:44px"><div class="pill"><h5>What is this 'Lorem Ipsum' or<br>'Lorum Ipsum' stuff</h5><p>In publishing and graphic design, placeholder text is commonly used to demonstrate the elements of a document or visual presentation, such as font, typography, and layout</p></div><div class="num"><b>1</b></div></div>
  <div class="pointer" style="left:166px;top:44px"><div class="pill"><h5>What is this 'Lorem Ipsum' or<br>'Lorum Ipsum' stuff?</h5><p>In publishing and graphic design, placeholder text is commonly used to demonstrate the elements of a document or visual presentation, such as font, typography, and layout</p></div><div class="num"><b>3</b></div></div>
  <div class="pointer" style="left:8px;top:116px"><div class="pill"><h5>What is this 'Lorem Ipsum' or<br>'Lorum Ipsum' stuff</h5><p>In publishing and graphic design, placeholder text is commonly used to demonstrate the elements of a document or visual presentation, such as font, typography, and layout</p></div><div class="num"><b>2</b></div></div>
  <div class="pointer" style="left:166px;top:116px"><div class="pill"><h5>What is this 'Lorem Ipsum' or<br>'Lorum Ipsum' stuff?</h5><p>In publishing and graphic design, placeholder text is commonly used to demonstrate the elements of a document or visual presentation, such as font, typography, and layout</p></div><div class="num"><b>4</b></div></div>
  <div class="brand" style="bottom:5px"><i></i>MORIVANE</div>
  <div class="team-mark" style="bottom:5px">Titans</div>
</section>

<!-- Meeting points -->
<section class="slide c2 r3">
  <h2 class="title" style="left:25px;top:10px;font-size:9.5px"><b>SOME POINTS</b> FOR A GOOD MEETING</h2>
  <p class="sub" style="left:25px;top:24px">Ignorant saw her her drawings marriage laughter.</p>
  <div class="bar-label" style="left:24px;top:54px;width:70px;background:var(--orange)">• Perhaps far</div>
  <div class="bar-sub" style="left:24px;top:64px;width:170px">Ignorant saw her her drawings marriage laughter</div>
  <p class="abs tiny" style="left:30px;top:73px;width:270px">• We come ready with clear goals, a short agenda and the numbers you need, so every minute of the meeting moves the plan forward and ends with agreed next steps.</p>
  <div class="bar-label" style="left:24px;top:107px;width:70px;background:var(--dark)">• Picture removal</div>
  <div class="bar-sub" style="left:24px;top:117px;width:170px">Ignorant saw her her drawings marriage laughter</div>
  <p class="abs tiny" style="left:30px;top:126px;width:270px">• We send notes the same day, with owners and dates for each task, so nothing is lost once the meeting ends.</p>
  <p class="abs tiny" style="left:30px;top:135px;width:270px">• A short follow-up call is booked before we leave the room to keep things on track.</p>
  <div class="brand"><i></i>MORIVANE</div>
  <div class="team-mark">Titans</div>
</section>

<!-- Only content -->
<section class="slide slide--orange c3 r3">
  <h2 class="abs" style="left:21px;top:18px;font-size:7.5px;font-weight:700;text-decoration:underline;color:var(--dark)">ONLY <span style="color:#fff;font-weight:400">CONTENT</span></h2>
  <p class="abs" style="left:21px;top:40px;font-size:6.5px;font-weight:700;color:var(--dark)">What is this ‘Lorem Ipsum’ or ‘Lorum Ipsum’ stuff?</p>
  <p class="abs" style="left:21px;top:73px;width:282px;font-size:6.3px;line-height:7px">In publishing and graphic design, placeholder text is commonly used to demonstrate the elements of a document or visual presentation, such as font, typography, and layout. Even though using “lorem ipsum” often arouses curiosity because of its resemblance to classical Latin, it is not intended to have meaning. Where text is visible in a document, people tend to focus on the textual content rather than upon overall presentation, so publishers use lorem ipsum when displaying a typeface or design elements and page layout in order to direct the focus to the publication style and not the meaning of the text.</p>
</section>

<!-- Key points -->
<section class="slide c1 r4">
  <svg class="abs" style="left:0;top:0" width="80" height="50" viewBox="0 0 80 50"><polygon points="0,30 20,0 30,0 6,38" fill="var(--dark)"/><polygon points="10,40 38,0 48,0 18,44" fill="var(--dark)"/><polygon points="56,10 64,0 76,0 64,18" fill="var(--orange)"/></svg>
  <svg class="abs" style="right:0;bottom:0" width="50" height="70" viewBox="0 0 50 70"><polygon points="50,0 50,14 10,70 0,70" fill="var(--dark)"/><polygon points="50,26 50,38 26,70 16,70" fill="var(--orange)"/></svg>
  <h2 class="title" style="left:79px;top:10px;font-size:10px">KEY <b>POINTS</b></h2>
  <p class="sub" style="left:79px;top:27px">Although moreover mistaken kindness me</p>
  <div class="brand" style="left:auto;right:16px;top:10px;bottom:auto"><i></i>MORIVANE</div>
  <div class="kp" style="left:28px;top:60px"><div class="dot" style="background:#96371a">1</div><h6>Inermis hendrerit vel cu</h6><p class="tiny">We bring new team gear to fans fast, with fair prices and clear care for the club's good name.</p></div>
  <div class="kp" style="left:28px;top:98px"><div class="dot" style="background:var(--orange)">2</div><h6>Id mel nibh posse copiosae</h6><p class="tiny">Our store runs day and night, so fans can buy from home, on the road or at the park.</p></div>
  <div class="kp" style="left:28px;top:136px"><div class="dot" style="background:var(--dark)">3</div><h6>Cu pri nostrum accusamus</h6><p class="tiny">Each sale is tracked so your club sees what fans love and what to make next season.</p></div>
  <div class="kp" style="left:164px;top:60px"><div class="dot" style="background:var(--dark)">4</div><h6>Cu pri nostrum accusamus</h6><p class="tiny">Special runs for big games and milestones sell out fast and lift fan spirit.</p></div>
  <div class="kp" style="left:164px;top:98px"><div class="dot" style="background:var(--orange)">5</div><h6>Inermis hendrerit vel cu</h6><p class="tiny">Returns are simple and free, which keeps fans happy and coming back.</p></div>
  <div class="kp" style="left:164px;top:136px"><div class="dot" style="background:#96371a">6</div><h6>Id mel nibh posse copiosae</h6><p class="tiny">Gift cards and bundles help fans share the game with friends and family.</p></div>
  <div class="team-mark" style="left:8px;right:auto;bottom:14px">Titans</div>
</section>

<!-- Sales chart -->
<section class="slide c2 r4">
  <h2 class="title" style="left:22px;top:9px;font-size:10px">SALES CHART</h2>
  <p class="sub" style="left:22px;top:23px;color:#444">Lorem ipsum dolor sit amet, alii aliquip ei vel</p>
  <div class="brand" style="left:auto;right:16px;top:10px;bottom:auto"><i></i>MORIVANE</div>
  <svg class="abs" style="left:8px;top:50px" width="306" height="100" viewBox="0 0 306 100" font-family="Open Sans" font-size="4.5">
    <g fill="var(--orange)" text-anchor="end">
      <text x="14" y="6">1000</text><text x="14" y="22">800</text><text x="14" y="38">600</text><text x="14" y="54">400</text><text x="14" y="70">200</text><text x="14" y="86">0</text>
    </g>
    <g fill="var(--orange)">
      <text x="286" y="6">20000</text><text x="286" y="22">15000</text><text x="286" y="38">10000</text><text x="286" y="54">5000</text><text x="286" y="86">0</text>
    </g>
    <line x1="18" y1="84" x2="282" y2="84" stroke="#ccc" stroke-width=".5"/>
    <g fill="var(--orange)">
      <rect x="24" y="48" width="4" height="36"/><rect x="45" y="42" width="4" height="42"/><rect x="66" y="35" width="4" height="49"/><rect x="87" y="56" width="4" height="28"/><rect x="108" y="52" width="4" height="32"/><rect x="129" y="40" width="4" height="44"/><rect x="150" y="54" width="4" height="30"/><rect x="171" y="44" width="4" height="40"/><rect x="192" y="58" width="4" height="26"/><rect x="213" y="52" width="4" height="32"/><rect x="234" y="38" width="4" height="46"/><rect x="255" y="50" width="4" height="34"/>
      <rect x="35" y="54" width="4" height="30"/><rect x="77" y="62" width="4" height="22"/><rect x="119" y="60" width="4" height="24"/><rect x="161" y="48" width="4" height="36"/><rect x="203" y="54" width="4" height="30"/><rect x="245" y="60" width="4" height="24"/>
    </g>
    <g fill="var(--dark)">
      <rect x="29" y="50" width="4" height="34"/><rect x="50" y="58" width="4" height="26"/><rect x="55" y="76" width="4" height="8"/><rect x="71" y="46" width="4" height="38"/><rect x="92" y="50" width="4" height="34"/><rect x="113" y="54" width="4" height="30"/><rect x="134" y="56" width="4" height="28"/><rect x="155" y="62" width="4" height="22"/><rect x="176" y="36" width="4" height="48"/><rect x="197" y="66" width="4" height="18"/><rect x="218" y="60" width="4" height="24"/><rect x="239" y="36" width="4" height="48"/><rect x="260" y="56" width="4" height="28"/>
    </g>
    <polyline points="26,52 47,60 68,58 89,60 110,56 131,52 152,58 173,50 194,46 215,52 236,44 257,48 270,42" fill="none" stroke="var(--dark)" stroke-width="1"/>
    <g fill="var(--dark)"><circle cx="26" cy="52" r="1.3"/><circle cx="68" cy="58" r="1.3"/><circle cx="131" cy="52" r="1.3"/><circle cx="173" cy="50" r="1.3"/><circle cx="215" cy="52" r="1.3"/><circle cx="270" cy="42" r="1.3"/></g>
    <g fill="var(--orange)" text-anchor="middle">
      <text x="30" y="94">Jan</text><text x="51" y="94">Feb</text><text x="72" y="94">Mar</text><text x="93" y="94">Apr</text><text x="114" y="94">May</text><text x="135" y="94">Jun</text><text x="156" y="94">Jul</text><text x="177" y="94">Aug</text><text x="198" y="94">Sep</text><text x="219" y="94">Oct</text><text x="240" y="94">Nov</text><text x="261" y="94">Dec</text>
    </g>
  </svg>
  <div class="bar-label" style="left:21px;top:149px;width:110px;height:9px;background:var(--orange)">• Next Target Month <span style="background:#fff;color:var(--orange);padding:0 2px">April</span></div>
  <p class="abs tiny" style="left:30px;top:162px;width:270px">Mirum sonet pertinax mel ad, vis in movet vocibus posidonium. <span style="color:var(--orange)">Mei te omittam offendit</span>, est ullum prodesset ea. Felis mazim lobortis et usu. Cum eu quas singulis neglegentur, est dicit utamur habemus in, et quas mollis mandamus mei.</p>
  <div class="team-mark" style="left:6px;right:auto;bottom:6px">Titans</div>
</section>

<!-- Thank you -->
<section class="slide slide--dark c3 r4">
  <h2 class="abs" style="left:19px;top:76px;font-family:'Raleway',sans-serif;font-weight:400;font-size:19px"><span style="color:var(--orange)">THANK</span> YOU!</h2>
  <div class="abs" style="left:50px;right:50px;top:138px;height:1px;background:#fff;opacity:.7"></div>
  <div class="contact" style="left:18px"><div class="ico"><svg width="10" height="12" viewBox="0 0 10 12"><path d="M5 12S1 7 1 4.5a4 4 0 018 0C9 7 5 12 5 12z" fill="#fff"/><circle cx="5" cy="4.5" r="1.5" fill="var(--orange)"/></svg></div><b>Our Location A</b><span>58 Corvel Lane<br>Ambrose City<br>ZIP 40210 - 40211</span></div>
  <div class="contact" style="left:93px"><div class="ico"><svg width="10" height="12" viewBox="0 0 10 12"><path d="M5 12S1 7 1 4.5a4 4 0 018 0C9 7 5 12 5 12z" fill="#fff"/><circle cx="5" cy="4.5" r="1.5" fill="var(--orange)"/></svg></div><b>Our Location B</b><span>92 Hollin Road<br>Ambrose City<br>ZIP 40210 - 40211</span></div>
  <div class="contact" style="left:168px"><div class="ico"><svg width="8" height="12" viewBox="0 0 8 12"><rect x="1" y="0.5" width="6" height="11" rx="1" fill="none" stroke="#fff" stroke-width="1"/><circle cx="4" cy="9.5" r=".7" fill="#fff"/></svg></div><b>Our Phone</b><span>(555) 014 2231<br>(555) 014 2232<br>(555) 014 2233</span></div>
  <div class="contact" style="left:243px"><div class="ico"><svg width="11" height="8" viewBox="0 0 11 8"><rect x=".5" y=".5" width="10" height="7" fill="#fff"/><path d="M.5 .5l5 4 5-4" fill="none" stroke="var(--orange)" stroke-width=".8"/></svg></div><b>Email / Website</b><span>hello@morivane.example<br>www.morivane.example</span></div>
</section>

</body>
</html>
```